Real Estate Listing Signs for standard Yard arms

I need real estate listing signs done, for the standard sized sign to be hung beneath a white yard arm. To match existing logo. Information to be included:
-Logo
-Business name
-Phone number
-Dorran Fitch Tundra Circle & Dorran Fitch realty logos (smaller print)

Colors to be Red and anywhere in the gray scale between black and white, or a combination of those.

Target Market(s)

Drive by visuals

Industry/Entity Type

Real Estate Agent

Colors

Designer to choose only greyscale colors for use in the design.

Requirements
Must have
• My Logo and business name in same/similar font to whats provided, the DF tundra circle logo (small on bottom or corner somewhere), My phone number, and a decent amount of red coloration on the sign.

```html
<!DOCTYPE html>
<html lang="en">
<head>
<meta charset="utf-8">
<title>Brannock Realty – Yard Sign</title>
<link rel="stylesheet" href="https://fonts.googleapis.com/css2?family=Open+Sans:wght@400;700&family=Oswald:wght@600&family=Montserrat:wght@700&display=swap">
<style>
  :root {
    --brand-red: #e3101c;
    --ink: #111111;
    --paper-top: #ffffff;
    --paper-bottom: #e2e2e2;
    --stage: #f2f2f2;
    --muted: #4a4a4a;
  }
  * { margin: 0; padding: 0; box-sizing: border-box; }
  html, body { width: 1200px; height: 888px; overflow: hidden; background: var(--stage); }
  .canvas { position: relative; width: 1200px; height: 888px; }
  .sign {
    position: absolute; left: 330px; top: 18px; width: 540px; height: 852px;
    background: linear-gradient(180deg, var(--paper-top) 0%, var(--paper-bottom) 100%);
    box-shadow: 0 2px 10px rgba(0,0,0,0.18);
  }
  .brand-mark {
    position: absolute; left: 210px; top: 90px; width: 120px; height: 120px;
    background: var(--brand-red);
  }
  .business-name {
    position: absolute; left: 0; top: 318px; width: 100%;
    text-align: center; font-family: "Open Sans", sans-serif; font-weight: 700;
    font-size: 68px; line-height: 94px; color: var(--ink); letter-spacing: 1px;
  }
  .call-rule {
    position: absolute; left: 0; top: 565px; width: 100%; height: 4px; background: var(--ink);
  }
  .call-tag { position: absolute; left: 135px; top: 540px; width: 270px; height: 52px; }
  .call-tag svg { position: absolute; inset: 0; }
  .call-tag span {
    position: absolute; inset: 0; display: flex; align-items: center; justify-content: center;
    font-family: "Montserrat", sans-serif; font-weight: 700; font-size: 28px;
    letter-spacing: 7px; color: #ffffff; padding-left: 7px;
  }
  .phone-band {
    position: absolute; left: 0; top: 576px; width: 100%; height: 138px;
    background: var(--brand-red); display: flex; align-items: center; justify-content: center;
  }
  .phone-number {
    font-family: "Oswald", sans-serif; font-weight: 600; font-size: 82px;
    color: #ffffff; letter-spacing: 1px;
  }
  .phone-rule {
    position: absolute; left: 0; top: 718px; width: 100%; height: 4px; background: var(--ink);
  }
  .partner {
    position: absolute; left: 0; top: 750px; width: 100%; text-align: center;
    font-family: "Open Sans", sans-serif; font-weight: 400; color: var(--muted);
  }
  .partner-name { font-size: 30px; line-height: 36px; text-transform: uppercase; letter-spacing: -0.5px; }
  .partner-sub { font-size: 13px; line-height: 18px; text-transform: uppercase; letter-spacing: 1px; }
</style>
</head>
<body>
<div class="canvas">
  <div class="sign">
    <div class="brand-mark"></div>
    <h1 class="business-name">BRANNOCK<br>REALTY</h1>

    <div class="call-rule"></div>
    <div class="phone-band">
      <span class="phone-number">(555)-014-2746</span>
    </div>
    <div class="call-tag">
      <svg viewBox="0 0 270 52" width="270" height="52" aria-hidden="true">
        <polygon points="24,0 246,0 270,26 246,52 24,52 0,26" fill="#111111"/>
      </svg>
      <span>CALL US</span>
    </div>
    <div class="phone-rule"></div>

    <div class="partner">
      <div class="partner-name">DF tundra circle</div>
      <div class="partner-sub">Dorran Fitch Realty</div>
    </div>
  </div>
</div>
</body>
</html>
```